lark to lead - dorian whitcombe personal speaking/consulting website

custom website for my personal speaking/consulting services brand, you can see the basic site we are using as a placeholder at www.larktolead.example now. I want to re-position this to more of a personal brand site and have video samples of speaking events, downloadable content, a video blog, and links to podcast. I really like the design of marcoveldin.example and the feature set should be fairly similar to his. I'll begin to compile more stock images etc. to use for sliders like he has done, for now we'll need to use stock imagery or existing photography from my social accounts. You can get a feel for social at all platforms/dwhitrealty i.e. facebook.com/dwhitrealty. the site should be primarily geared toward showcasing speaking/consulting services and content, as well as be flexible to allow for additional downloadables etc. in the future.

Target Market(s)

entrepreneurs and leaders looking to grow themselves, their business, and those they lead.

Coding

Coded - Design and coding required

Number of Pages Required

3 page

Font styles to use
Sans Serif

Colors

Designer to choose colors to be used in the design.

Requirements
Must have
• modern slick design, video blog, podcast feed, registration for people to subscribe to newsletter

```html
<!DOCTYPE html>
<html lang="en">
<head>
<meta charset="utf-8">
<title>Dorian Whitcombe — Lark to Lead</title>
<link href="https://fonts.googleapis.com/css2?family=Josefin+Sans:wght@300;400;600;700&family=Raleway:wght@400;500;600;700&display=swap" rel="stylesheet">
<style>
:root{
  --orange:#e0701f;
  --orange-dark:#c95f14;
  --ink:#1d1d1d;
  --text:#555;
  --light:#f1f1f1;
  --paper:#ffffff;
  --night:#1f1f1f;
  --footer:#1b1b1b;
}
*{box-sizing:border-box;margin:0;padding:0}
html,body{width:1200px;height:4591px;overflow:hidden}
body{font-family:"Raleway",sans-serif;color:var(--text);background:var(--paper);position:relative}
.abs{position:absolute}
h1,h2,h3,.brand,.tile-label{font-family:"Josefin Sans",sans-serif}
.accent{color:var(--orange);font-weight:300}
.btn{position:absolute;background:var(--orange);color:#fff;font:600 13px "Raleway",sans-serif;display:flex;align-items:center;justify-content:center;letter-spacing:.3px;text-transform:uppercase}
.field{position:absolute;background:#fff;border:1px solid #ddd;font-size:13px;color:#666;display:flex;align-items:center;padding-left:16px}

/* header */
.site-header{position:absolute;left:0;top:0;width:1200px;height:87px;background:#fff}
.brand{left:145px;top:26px;font-size:31px;font-weight:600;color:var(--ink)}
.main-nav{left:484px;top:36px;display:flex;gap:30px;font-size:13px;color:#333}
.listen-btn{left:878px;top:25px;width:176px;height:37px;border-radius:20px;font-size:13px;text-transform:none;font-weight:500;gap:8px}
.listen-btn i{width:16px;height:16px;border:2px solid #fff;border-radius:50%}

/* hero */
.hero{left:0;top:87px;width:1200px;height:565px;background:radial-gradient(ellipse at 50% 90%,#7a5a3a 0%,#3a2e28 40%,#141418 85%)}
.hero h1{position:absolute;left:0;width:1200px;top:280px;text-align:center;color:#fff;font-size:44px;font-weight:700;line-height:50px;text-transform:uppercase}

/* scroll cue */
.scroll-cue{left:555px;top:607px;width:90px;height:90px;border-radius:50%;background:var(--light)}

/* about */
.about{left:0;top:652px;width:1200px;height:646px;background:var(--light)}
.about-photo{left:0;top:60px;width:500px;height:586px;background:linear-gradient(160deg,#3b2d27,#7b5a48 45%,#2d3548);border-radius:0 0 60px 0}
.about h2{position:absolute;left:552px;top:122px;font-size:42px;font-weight:700;color:var(--ink)}
.about p{position:absolute;left:552px;width:500px;font-size:12.5px;line-height:32px;color:#555}
.about-side{left:1055px;top:120px;width:140px;height:440px;font:700 120px "Josefin Sans",sans-serif;color:#e4e4e4;writing-mode:vertical-rl;transform:rotate(180deg);line-height:140px}
.listing-badge{left:552px;top:497px;width:172px;height:43px;border:1px solid #999;border-radius:6px;background:#2b2b2b}

/* blog */
.blog{left:0;top:1298px;width:1200px;height:1016px;background:var(--night)}
.blog h2{left:0;width:1200px;top:62px;text-align:center;font-size:42px;color:#fff;font-weight:700}
.blog-card{left:144px;top:152px;width:912px;height:785px;background:#fff}
.blog-video{left:11px;top:11px;width:890px;height:427px;background:linear-gradient(180deg,#8a8a8a,#4a4a4a 55%,#2a2a2a)}
.play{left:400px;top:168px;width:88px;height:88px;border-radius:50%;background:#fff}
.blog-card h3{position:absolute;left:0;width:912px;top:483px;text-align:center;font:600 21px "Raleway",sans-serif;color:var(--ink)}
.blog-card p{position:absolute;left:50px;width:812px;top:530px;text-align:center;font-size:12.5px;line-height:27px;color:#555}

/* services */
.services{left:0;top:2314px;width:1200px;height:751px;background:#fafafa}
.services h2{left:0;width:1200px;top:88px;text-align:center;font-size:42px;font-weight:700;color:var(--ink)}
.service-card{position:absolute;top:184px;width:278px;height:470px;background:#fff;box-shadow:0 0 0 1px #f0f0f0}
.service-img{left:0;top:0;width:278px;height:166px}
.service-card h3{position:absolute;top:195px;width:100%;text-align:center;font:600 15px "Raleway",sans-serif;color:var(--ink)}
.service-card p{position:absolute;left:25px;width:228px;top:245px;text-align:center;font-size:12px;line-height:23.5px;color:#555}
.service-card .btn{left:63px;top:404px;width:150px;height:43px}

/* newsletter */
.newsletter{left:0;top:3065px;width:1200px;height:303px;background:#fff}
.newsletter h2{left:0;width:1200px;top:68px;text-align:center;font-size:42px;font-weight:700;color:var(--ink)}
.newsletter .sub{left:0;width:1200px;top:142px;text-align:center;font-size:11px;color:#444}

/* tiles */
.tile{top:3368px;width:600px;height:424px}
.tile-label{position:absolute;border:2px solid #fff;display:flex;align-items:center;justify-content:center;font-size:40px;font-weight:300;letter-spacing:2px}

/* team */
.team{left:0;top:3792px;width:1200px;height:496px;background:linear-gradient(180deg,#9a9a9a,#4a4a4a 60%,#2a2a2a)}

/* footer */
.site-footer{left:0;top:4288px;width:1200px;height:303px;background:var(--footer);color:#fff}
.contact-item{position:absolute;top:62px;display:flex;gap:16px;align-items:center;font-size:12px;line-height:22px}
.contact-item svg{flex:none}
.divider{position:absolute;top:62px;width:1px;height:44px;background:#444}
.footer-nav{left:0;width:1200px;top:136px;text-align:center;font-size:15px;word-spacing:6px}
.copy{left:0;width:1200px;top:176px;text-align:center;font-size:11px;color:#ddd}
.social{position:absolute;top:213px;width:36px;height:36px;border-radius:50%;background:var(--orange)}
</style>
</head>
<body>

<header class="site-header">
  <div class="abs brand">Dorian Whitcombe</div>
  <nav class="abs main-nav"><span>HOME</span><span>ABOUT</span><span>PODCAST</span><span>EVENTS</span><span>CONTACT</span></nav>
  <div class="btn listen-btn"><i></i>Listen to Podcast</div>
</header>

<section class="abs hero" role="img" aria-label="Man raising his arms above a night city skyline">
  <h1>The place where entrepreneurs<br>come to become leaders.</h1>
  <div class="field" style="left:310px;top:413px;width:220px;height:40px">Your Name</div>
  <div class="field" style="left:543px;top:413px;width:220px;height:40px">Your Email</div>
  <div class="btn" style="left:775px;top:413px;width:115px;height:40px">Subscribe</div>
</section>

<section class="abs about">
  <div class="abs about-photo" role="img" aria-label="Portrait of Dorian Whitcombe"></div>
  <div class="abs about-side">ABOUT</div>
  <h2>ABOUT <span class="accent">ME</span></h2>
  <p style="top:190px">Sed ut perspiciatis unde omnis iste natus error sit voluptatem accusantium doloremque laudantium, totam rem aperiam, eaque ipsa quae ab illo inventore veritatis et quasi architecto beatae vitae dicta sunt explicabo. Nemo enim ipsam voluptatem quia voluptas sit aspernatur aut odit aut fugit, sed quia consequuntur magni dolores eos qui ratiem sequi nesciunt.</p>
  <p style="top:352px">Neque porro quisquam est, qui dolorem ipsum quia dolor sit amet, consectetur, adipisci velit, sed quia non numquam eius modi tempora incidunt ut labore et dolore magnam aliquam quaerat voluptatem</p>
  <div class="abs listing-badge" role="img" aria-label="Podcast listing badge"></div>
  <div class="btn" style="left:752px;top:497px;width:158px;height:43px;gap:8px">Learn More
    <svg width="14" height="14" viewBox="0 0 14 14"><circle cx="7" cy="7" r="7" fill="#fff"/><path d="M5 4l3 3-3 3" stroke="#e0701f" stroke-width="2" fill="none"/></svg></div>
</section>

<div class="abs scroll-cue">
  <svg width="90" height="90" viewBox="0 0 90 90"><rect x="33" y="16" width="24" height="36" rx="12" fill="none" stroke="#222" stroke-width="2"/><line x1="45" y1="23" x2="45" y2="31" stroke="#222" stroke-width="2"/><path d="M39 58l6 5 6-5M39 65l6 5 6-5" stroke="#222" stroke-width="2" fill="none"/></svg>
</div>

<section class="abs blog">
  <h2 class="abs">OUR <span class="accent">BLOG</span></h2>
  <article class="abs blog-card">
    <div class="abs blog-video" role="img" aria-label="Audience watching a speaker at a conference">
      <div class="abs play"><svg width="88" height="88" viewBox="0 0 88 88"><path d="M38 34l16 10-16 10z" fill="#e0701f"/></svg></div>
    </div>
    <h3>QUIS AUTEM VEL EUM IURE REPREHENDERIT QUI IN EA VOLUPTATE VELIT ESSE</h3>
    <p>At vero eos et accusamus et iusto odio dignissimos ducimus qui blanditiis praesentium voluptatum deleniti atque corrupti quos dolores et quas molestias excepturi sint occaecati cupiditate non provident, similique sunt in culpa qui officia deserunt mollitia animi, id est laborum et dolorum fuga. Et harum quidem rerum facilis est et expedita distinctio. Nam libero tempore, cum soluta nobis est eligendi optio cumque nihil impedit quo minus id quod maxime placeat facere possimus.</p>
    <div class="btn" style="left:381px;top:670px;width:151px;height:47px">View More</div>
  </article>
</section>

<section class="abs services">
  <h2 class="abs">SPEAKING / <span class="accent">CONSULTING SERVICES</span></h2>
  <div class="service-card" style="left:148px">
    <div class="abs service-img" role="img" aria-label="Hands working on a laptop beside a calculator" style="background:linear-gradient(135deg,#c9a27a,#6e5a4a)"></div>
    <h3>ACCUSANTIUM DOLOREMQUE</h3>
    <p>Sed ut perspiciatis unde omnis iste natus error sit voluptatem accusantium doloremque laudantium, totam rem aperiam, eaque ipsa quae ab illo inventore veritatis et quasi architecto beatae vitae dicta sunt explicabo</p>
    <div class="btn">Learn More</div>
  </div>
  <div class="service-card" style="left:461px">
    <div class="abs service-img" role="img" aria-label="Speaker presenting to a large audience" style="background:linear-gradient(135deg,#2a3a6a,#b04a4a)"></div>
    <h3>NUMQUAM EIUS MODI</h3>
    <p>Nemo enim ipsam voluptatem quia voluptas sit aspernatur aut odit aut fugit, sed quia consequuntur magni dolores eos qui ratione voluptatem sequi nesciunt. Neque porro quisquam est, qui dolorem ipsum quia dolor sit amet</p>
    <div class="btn">Learn More</div>
  </div>
  <div class="service-card" style="left:774px">
    <div class="abs service-img" role="img" aria-label="Team meeting around a table with laptops" style="background:linear-gradient(135deg,#b8c2cc,#5a6068)"></div>
    <h3>VOLUPTATE VELIT ESSE</h3>
    <p>Et harum quidem rerum facilis est et expedita distinctio. Nam libero tempore, cum soluta nobis est eligendi optio cumque nihil impedit quo minus id quod maxime placeat facere possimus, omnis voluptas assumenda</p>
    <div class="btn">Learn More</div>
  </div>
</section>

<section class="abs newsletter">
  <h2 class="abs">SUBSCRIBE TO <span class="accent">OUR NEWSLETTER</span></h2>
  <div class="abs sub">EXCEPTEUR SINT OCCAECAT CUPIDATAT NON PROIDENT SUNT IN CULPA QUI OFFICIA</div>
  <div class="field" style="left:221px;top:197px;width:310px;height:40px">Your Name</div>
  <div class="field" style="left:542px;top:197px;width:310px;height:40px">Your Email</div>
  <div class="btn" style="left:863px;top:197px;width:116px;height:40px">Submit</div>
</section>

<div class="abs tile" style="left:0;background:linear-gradient(135deg,#e89a55,#d9782e)" role="img" aria-label="Off-road truck parked at an event">
  <div class="tile-label" style="left:190px;top:167px;width:220px;height:88px;color:#333;background:#fff;box-shadow:0 0 0 8px rgba(255,255,255,.35)">ABOUT</div>
</div>
<div class="abs tile" style="left:600px;background:linear-gradient(135deg,#6b5a4a,#c9b59a 60%,#8a7a6a)" role="img" aria-label="Smiling woman and girl with face paint">
  <div class="tile-label" style="left:175px;top:175px;width:250px;height:72px;color:#fff;background:rgba(0,0,0,.25)">PODCAST</div>
</div>

<div class="abs team" role="img" aria-label="Group photo of a real estate team at an awards event"></div>

<footer class="abs site-footer">
  <div class="contact-item" style="left:253px">
    <svg width="34" height="34" viewBox="0 0 34 34"><circle cx="17" cy="17" r="16" fill="none" stroke="#fff" stroke-width="1.5"/><path d="M17 10a5 5 0 0 1 5 5c0 4-5 9-5 9s-5-5-5-9a5 5 0 0 1 5-5z" fill="none" stroke="#fff" stroke-width="1.5"/><circle cx="17" cy="15" r="1.6" fill="#fff"/></svg>
    <div>124,Sed ut perspiciatis unde<br>omnis iste natus..</div>
  </div>
  <div class="divider" style="left:515px"></div>
  <div class="contact-item" style="left:546px">
    <svg width="34" height="34" viewBox="0 0 34 34"><circle cx="17" cy="17" r="16" fill="none" stroke="#fff" stroke-width="1.5"/><path d="M12 11c1-1 2-1 3 0l1 2-1.5 1.5c.8 2 2 3.2 4 4L20 17l2 1c1 1 1 2 0 3-2 2-6 0-8-2s-4-6-2-8z" fill="#fff"/></svg>
    <div>Phone<br>1 888 888 8888</div>
  </div>
  <div class="divider" style="left:712px"></div>
  <div class="contact-item" style="left:742px">
    <svg width="34" height="34" viewBox="0 0 34 34"><circle cx="17" cy="17" r="16" fill="none" stroke="#fff" stroke-width="1.5"/><rect x="10" y="12" width="14" height="10" fill="#fff"/><path d="M10 12l7 6 7-6" stroke="#1b1b1b" stroke-width="1.3" fill="none"/></svg>
    <div>Email<br>hello@larktolead.example</div>
  </div>
  <div class="abs footer-nav">HOME &nbsp;/&nbsp; ABOUT &nbsp;/&nbsp; PODCAST &nbsp;/&nbsp; EVENTS &nbsp;/&nbsp; CONTACT</div>
  <div class="abs copy">Copyrights © 2019, Lark to Lead All Rights Reserved.</div>
  <div class="social" style="left:540px"></div>
  <div class="social" style="left:582px"></div>
  <div class="social" style="left:624px"></div>
</footer>

</body>
</html>
```